Online store website

Online store dealing on hoodies, joggers, trainers, baseball caps, trucker caps, winter hats, waist bands, jewelry sports and yoga suits , all women and men accessories.
All are my brand name Kelvo-trabrand.
I have a domain already

```html
<!DOCTYPE html>
<html lang="en">
<head>
<meta charset="utf-8">
<title>Kelvo-trabrand — Online Store</title>
<link href="https://fonts.googleapis.com/css2?family=Oswald:wght@400;500;600;700&family=Poppins:wght@400;500;600;700&display=swap" rel="stylesheet">
<style>
:root{
  --wine:#8c1230;
  --wine-dark:#6e0d25;
  --navy:#1c1f33;
  --ink:#1d1d22;
  --muted:#6b6b75;
  --soft:#f2f2f4;
  --line:#e3e3e8;
  --white:#ffffff;
}
*{box-sizing:border-box;margin:0;padding:0}
html,body{width:1200px;height:4120px;overflow:hidden}
body{position:relative;background:var(--white);font-family:'Poppins',sans-serif;color:var(--ink)}
.abs{position:absolute}
.heading{font-family:'Oswald',sans-serif;font-weight:600;text-transform:uppercase;letter-spacing:.5px}
.btn{display:inline-block;font-family:'Poppins',sans-serif;font-weight:600;font-size:14px;padding:12px 26px;border-radius:6px;white-space:nowrap}
.btn-dark{background:var(--navy);color:var(--white)}
.btn-white{background:var(--white);color:var(--ink)}
.section-title{text-align:center;font-size:34px;color:var(--ink)}
.title-bar{width:70px;height:3px;background:var(--wine);margin:10px auto 0}
.photo{border-radius:14px}

/* header */
.site-header{left:0;top:0;width:1200px;height:128px;background:var(--white);box-shadow:0 2px 10px rgba(0,0,0,.06)}
.brand{left:60px;top:26px;display:flex;align-items:center;gap:12px}
.brand-square{width:40px;height:40px;background:var(--wine)}
.brand-name{font-family:'Oswald',sans-serif;font-weight:700;font-size:26px;color:var(--navy);line-height:1}
.brand-name small{display:block;font-size:11px;font-weight:700;letter-spacing:2px;margin-top:3px}
.nav{left:430px;top:76px;display:flex;gap:62px;font-size:15px;color:var(--ink)}
.nav .active{color:var(--wine);font-weight:600;border-bottom:2px solid var(--wine);padding-bottom:6px}
.search{left:700px;top:22px;width:220px;height:34px;border:1px solid var(--line);border-radius:6px;font-size:12px;color:var(--muted);padding:8px 12px}
.search svg{position:absolute;right:10px;top:9px}
.icon-box{top:22px;width:34px;height:34px;border:1px solid var(--line);border-radius:6px;display:flex;align-items:center;justify-content:center}

/* hero */
.hero{left:0;top:128px;width:1200px;height:472px;background:var(--soft);overflow:hidden}
.hero-photo{left:600px;top:0;width:600px;height:472px;background:linear-gradient(160deg,#e9e6e2,#d8d2cc 55%,#c9c3bf)}
.hero-shape{left:0;top:0}
.hero-copy{left:60px;top:80px;color:var(--white);width:480px}
.hero-kicker{font-family:'Oswald',sans-serif;font-size:20px;font-weight:500;letter-spacing:1px}
.hero-title{font-size:46px;line-height:1.15;margin-top:10px}
.hero-sub{font-size:14px;margin-top:14px}
.hero-copy .btn{margin-top:20px}
.hero-offer{left:214px;top:392px;font-size:13px;font-weight:700;color:var(--ink);white-space:nowrap}
.hero-offer span{color:var(--wine)}
.hero-code{left:214px;top:416px;font-size:12px;font-weight:600;color:var(--ink);text-decoration:underline;white-space:nowrap}

/* categories */
.cat-title{left:0;top:676px;width:1200px}
.cat-sub{left:0;top:758px;width:1200px;text-align:center;font-size:14px;color:var(--muted)}
.cat-list{left:82px;top:800px;display:flex;gap:22px}
.cat-card{width:190px}
.cat-img{width:190px;height:230px;border-radius:10px}
.cat-card.featured .cat-img{outline:2px solid var(--wine);outline-offset:3px}
.cat-label{font-size:13px;font-weight:500;text-align:center;margin-top:16px}
.cat-card.featured .cat-label{color:var(--wine);font-weight:600}
.cat-badge{position:absolute;left:596px;top:995px;width:46px;height:46px;border-radius:50%;background:var(--wine);display:flex;align-items:center;justify-content:center}

/* about */
.about-back{left:110px;top:1160px;width:440px;height:250px;background:linear-gradient(135deg,#3a3a42,#7a6e70 50%,#b9a9ab)}
.about-front{left:288px;top:1270px;width:316px;height:330px;background:linear-gradient(150deg,#c23a4d,#3a4a8a 55%,#2a2a30);border:8px solid var(--white);box-shadow:0 6px 18px rgba(0,0,0,.15)}
.about-copy{left:676px;top:1248px;width:440px}
.about-copy h2{font-size:32px}
.about-copy .title-bar{margin:10px 0 22px}
.about-copy p{font-size:13px;line-height:1.75;color:var(--muted);margin-bottom:14px}

/* partners */
.partners{left:140px;top:1698px;width:920px;display:flex;justify-content:space-between;align-items:center}
.partner{font-size:26px;font-weight:700;color:var(--ink);width:150px;text-align:center}
.partner.boxed{background:var(--white);box-shadow:0 4px 16px rgba(0,0,0,.12);border-radius:10px;padding:22px 0}
.scroll-hint{left:588px;top:1816px}

/* new arrivals */
.arrivals{left:0;top:1862px;width:1200px;height:578px;background:var(--soft)}
.arr-title{left:0;top:1918px;width:1200px}
.arr-list{left:108px;top:2012px;display:flex;gap:26px}
.prod{width:230px;height:372px;background:var(--white);border-radius:12px;padding:10px;text-align:center;position:relative}
.prod.featured{outline:2px solid var(--wine)}
.prod-img{height:210px;border-radius:8px}
.prod-name{font-size:14px;font-weight:500;margin-top:16px}
.prod-price{font-size:15px;font-weight:700;margin-top:8px}
.prod-actions{display:flex;justify-content:center;gap:8px;margin-top:14px}
.prod-actions span{width:30px;height:30px;border-radius:6px;background:var(--wine);display:flex;align-items:center;justify-content:center}
.prod-tag{position:absolute;left:18px;top:18px;background:var(--wine);color:var(--white);font-size:10px;padding:3px 8px;border-radius:3px}
.side-arrows{left:1128px;top:2152px;display:flex;flex-direction:column;gap:8px}
.side-arrows span{width:30px;height:30px;border-radius:6px;display:flex;align-items:center;justify-content:center}
.side-arrows .on{background:var(--wine)}
.side-arrows .off{background:#e8c9d1}
.scroll-hint-2{left:588px;top:2394px}

/* product of month */
.potm{left:0;top:2440px;width:1200px;height:510px;overflow:hidden}
.potm-photo{left:560px;top:0;width:640px;height:510px;background:linear-gradient(120deg,#2b2626,#5a3a30 35%,#c0662e 60%,#2c5c8a 85%,#1a1a1f)}
.potm-band{left:0;top:0}
.potm-copy{left:56px;top:84px;width:460px;color:var(--white)}
.potm-copy h2{font-size:32px}
.potm-copy p{font-size:13px;line-height:1.7;margin-top:14px;opacity:.9}
.potm-deal{display:flex;align-items:flex-end;gap:14px;margin-top:26px}
.potm-deal .big{font-family:'Oswald',sans-serif;font-size:60px;font-weight:700;line-height:1}
.potm-deal .small{font-family:'Oswald',sans-serif;font-size:16px;padding-bottom:8px}
.potm-note{font-size:12px;margin-top:8px}
.potm-copy .btn{margin-top:26px;font-size:13px;padding:10px 22px}

/* testimonials */
.rev-title{left:0;top:3010px;width:1200px}
.rev-list{left:112px;top:3104px;display:flex;gap:32px}
.review{width:300px;height:356px;background:var(--white);border-radius:12px;box-shadow:0 4px 18px rgba(0,0,0,.08);padding:28px 28px}
.review.featured{outline:2px solid #d9a3b1}
.review p{font-size:13px;line-height:1.75;color:var(--muted)}
.stars{display:flex;gap:4px;margin-top:18px}
.reviewer{display:flex;align-items:center;gap:12px;margin-top:20px}
.avatar{width:44px;height:44px;border-radius:50%;background:linear-gradient(135deg,#c9b8ae,#8d7a70)}
.reviewer b{font-size:13px;display:block}
.reviewer small{font-size:10px;color:var(--muted)}
.rev-arrows{left:1128px;top:3250px}

/* newsletter */
.newsletter{left:0;top:3540px;width:1200px;height:172px;background:var(--navy)}
.nl-title{left:60px;top:3584px;color:var(--white);font-size:30px;line-height:1.25;letter-spacing:1px}
.nl-label{left:508px;top:3572px;color:var(--white);font-size:13px;font-weight:600}
.nl-form{left:508px;top:3604px;display:flex}
.nl-input{width:530px;height:52px;background:var(--white);border-radius:6px 0 0 6px;padding:16px 18px;font-size:13px;color:var(--muted)}
.nl-btn{width:52px;height:52px;background:var(--wine);border-radius:0 6px 6px 0;display:flex;align-items:center;justify-content:center}

/* footer */
.foot-brand{left:60px;top:3756px}
.socials{left:60px;top:3850px;display:flex;gap:10px}
.socials span{width:30px;height:30px;border-radius:50%;background:var(--wine)}
.foot-col{top:3758px}
.foot-col h4{font-family:'Oswald',sans-serif;font-weight:600;font-size:17px;text-transform:uppercase;letter-spacing:.5px}
.foot-col .title-bar{margin:6px 0 14px;width:54px}
.foot-col li{list-style:none;font-size:13px;color:var(--ink);margin-bottom:9px;display:flex;align-items:center;gap:8px}
.foot-col li::before{content:"";width:5px;height:5px;border-radius:50%;background:var(--wine)}
.payments{left:300px;top:4010px;display:flex;gap:10px}
.payments span{width:60px;height:30px;border-radius:5px;background:#e9e9ee;border:1px solid var(--line)}
.bottom-bar{left:0;top:4080px;width:1200px;height:40px;background:var(--navy);color:var(--white);font-size:11px;display:flex;justify-content:space-between;align-items:center;padding:0 60px}
</style>
</head>
<body>

<!-- Header -->
<header class="site-header abs">
  <div class="brand abs"><span class="brand-square"></span><div class="brand-name">KELVO-TRA<small>BRAND</small></div></div>
  <div class="search abs">Search<svg width="14" height="14" viewBox="0 0 14 14"><circle cx="6" cy="6" r="4.5" fill="none" stroke="#6b6b75" stroke-width="1.5"/><line x1="9.5" y1="9.5" x2="13" y2="13" stroke="#6b6b75" stroke-width="1.5"/></svg></div>
  <div class="icon-box abs" style="left:934px"><svg width="16" height="16" viewBox="0 0 16 16"><path d="M8 14 2 8a3.3 3.3 0 0 1 6-4 3.3 3.3 0 0 1 6 4z" fill="#8c1230"/></svg></div>
  <div class="icon-box abs" style="left:976px"><svg width="16" height="16" viewBox="0 0 16 16"><path d="M1 2h2l2 8h8l2-6H4" fill="none" stroke="#1c1f33" stroke-width="1.6"/><circle cx="6" cy="13" r="1.4" fill="#1c1f33"/><circle cx="12" cy="13" r="1.4" fill="#1c1f33"/></svg></div>
  <div class="icon-box abs" style="left:1018px"><svg width="16" height="16" viewBox="0 0 16 16"><circle cx="8" cy="5" r="3" fill="none" stroke="#1c1f33" stroke-width="1.6"/><path d="M2 15c1-4 11-4 12 0" fill="none" stroke="#1c1f33" stroke-width="1.6"/></svg></div>
  <nav class="nav abs"><span class="active">Home</span><span>Shop By Categories</span><span>Products</span><span>Reviews</span><span>Contact Us</span></nav>
</header>

<!-- Hero -->
<section class="hero abs">
  <div class="hero-photo abs" role="img" aria-label="Three women in fitted activewear sets posing together"></div>
  <svg class="hero-shape abs" width="660" height="472" viewBox="0 0 660 472"><polygon points="0,0 560,0 640,180 560,360 200,360 200,472 0,472" fill="#8c1230"/></svg>
  <div class="hero-copy abs">
    <div class="hero-kicker">STYLE REDEFINED</div>
    <h1 class="hero-title heading">Trendy Fashion<br>For Every Occasion</h1>
    <p class="hero-sub">Shop Hoodies, Joggers, Trainers, Caps &amp; More</p>
    <span class="btn btn-dark">Discover Your Style</span>
  </div>
  <div class="hero-offer abs"><span>✦</span> GET 10% OFF YOUR FIRST ORDER:</div>
  <div class="hero-code abs">Use Code: WELCOME10</div>
</section>

<!-- Featured categories -->
<h2 class="cat-title section-title heading abs">Featured Categories<div class="title-bar"></div></h2>
<p class="cat-sub abs">Visit our shop to see amazing creations from our designers.</p>
<div class="cat-list abs">
  <div class="cat-card"><div class="cat-img" role="img" aria-label="Man wearing a dark hoodie" style="background:linear-gradient(160deg,#d9d6d3,#4a4a50)"></div><div class="cat-label">Hoodies &amp; Sweatshirts</div></div>
  <div class="cat-card"><div class="cat-img" role="img" aria-label="Woman stretching in a sports suit" style="background:linear-gradient(160deg,#cfd3d8,#3a3f48)"></div><div class="cat-label">Activewear &amp; Sports Suits</div></div>
  <div class="cat-card featured"><div class="cat-img" role="img" aria-label="Legs in beige trousers and trainers" style="background:linear-gradient(160deg,#f0ebe4,#cbbfae)"></div><div class="cat-label">Footwear</div></div>
  <div class="cat-card"><div class="cat-img" role="img" aria-label="Woman in a yellow winter jacket and knit hat" style="background:linear-gradient(160deg,#e7e2da,#d69a3a)"></div><div class="cat-label">Winter Collection</div></div>
  <div class="cat-card"><div class="cat-img" role="img" aria-label="Close-up of a waistband on cream trousers" style="background:linear-gradient(160deg,#b24a4a,#e7d6c6)"></div><div class="cat-label">Waistbands</div></div>
</div>
<div class="cat-badge"><svg width="20" height="20" viewBox="0 0 20 20"><path d="M3 8h14l-1 9H4zM7 8V5a3 3 0 0 1 6 0v3" fill="none" stroke="#fff" stroke-width="1.8"/></svg></div>

<!-- About -->
<div class="about-back photo abs" role="img" aria-label="Clothing store interior with mannequins"></div>
<div class="about-front photo abs" role="img" aria-label="Racks of colourful jackets and folded garments"></div>
<div class="about-copy abs">
  <h2 class="heading">Who We Are</h2>
  <div class="title-bar"></div>
  <p>Sed ut perspiciatis unde omnis iste natus error sit voluptatem accusantium doloremque laudantium, totam rem aperiam, eaque ipsa quae ab illo inventore veritatis et quasi architecto beatae vitae.</p>
  <p>Nemo enim ipsam voluptatem quia voluptas sit aspernatur aut odit aut fugit, sed quia consequuntur magni dolores eos qui ratione voluptatem sequi nesciunt.</p>
  <span class="btn btn-dark">Explore More</span>
</div>

<!-- Partners -->
<div class="partners abs">
  <div class="partner">Linqo</div>
  <div class="partner">Vantora</div>
  <div class="partner boxed">Paylume</div>
  <div class="partner">Roomly</div>
  <div class="partner">Marketra</div>
</div>
<svg class="scroll-hint abs" width="24" height="24" viewBox="0 0 24 24"><path d="M7 10l5 5 5-5" fill="none" stroke="#1c1f33" stroke-width="2"/></svg>

<!-- New arrivals -->
<section class="arrivals abs"></section>
<h2 class="arr-title section-title heading abs">New Arrivals<div class="title-bar"></div></h2>
<div class="arr-list abs">
  <div class="prod"><div class="prod-img" role="img" aria-label="Man seated in grey joggers and jacket" style="background:linear-gradient(160deg,#d7d4cf,#6a655f)"></div><div class="prod-name">Urban Pulse Joggers</div><div class="prod-price">$98.00</div><div class="prod-actions"><span><svg width="14" height="14" viewBox="0 0 16 16"><path d="M8 14 2 8a3.3 3.3 0 0 1 6-4 3.3 3.3 0 0 1 6 4z" fill="#fff"/></svg></span><span><svg width="14" height="14" viewBox="0 0 16 16"><path d="M1 2h2l2 8h8l2-6H4" fill="none" stroke="#fff" stroke-width="1.8"/></svg></span><span><svg width="14" height="14" viewBox="0 0 14 14"><circle cx="6" cy="6" r="4.5" fill="none" stroke="#fff" stroke-width="1.8"/><line x1="9.5" y1="9.5" x2="13" y2="13" stroke="#fff" stroke-width="1.8"/></svg></span></div></div>
  <div class="prod featured"><span class="prod-tag">Best Sellers</span><div class="prod-img" role="img" aria-label="Rolled waistbands in many colours" style="background:linear-gradient(135deg,#d8452f,#e69a2a 35%,#2b7a8c 65%,#33395a)"></div><div class="prod-name">Waistbands</div><div class="prod-price">$98.00</div><div class="prod-actions"><span><svg width="14" height="14" viewBox="0 0 16 16"><path d="M8 14 2 8a3.3 3.3 0 0 1 6-4 3.3 3.3 0 0 1 6 4z" fill="#fff"/></svg></span><span><svg width="14" height="14" viewBox="0 0 16 16"><path d="M1 2h2l2 8h8l2-6H4" fill="none" stroke="#fff" stroke-width="1.8"/></svg></span><span><svg width="14" height="14" viewBox="0 0 14 14"><circle cx="6" cy="6" r="4.5" fill="none" stroke="#fff" stroke-width="1.8"/><line x1="9.5" y1="9.5" x2="13" y2="13" stroke="#fff" stroke-width="1.8"/></svg></span></div></div>
  <div class="prod"><div class="prod-img" role="img" aria-label="Woman in a yoga pose wearing a yoga suit" style="background:linear-gradient(160deg,#eee9e2,#c8b9a6)"></div><div class="prod-name">Yoga Suits</div><div class="prod-price">$18.00</div><div class="prod-actions"><span><svg width="14" height="14" viewBox="0 0 16 16"><path d="M8 14 2 8a3.3 3.3 0 0 1 6-4 3.3 3.3 0 0 1 6 4z" fill="#fff"/></svg></span><span><svg width="14" height="14" viewBox="0 0 16 16"><path d="M1 2h2l2 8h8l2-6H4" fill="none" stroke="#fff" stroke-width="1.8"/></svg></span><span><svg width="14" height="14" viewBox="0 0 14 14"><circle cx="6" cy="6" r="4.5" fill="none" stroke="#fff" stroke-width="1.8"/><line x1="9.5" y1="9.5" x2="13" y2="13" stroke="#fff" stroke-width="1.8"/></svg></span></div></div>
  <div class="prod"><div class="prod-img" role="img" aria-label="Woman stretching outdoors in a sports suit" style="background:linear-gradient(160deg,#e9e4dc,#a99884)"></div><div class="prod-name">Sports Suits</div><div class="prod-price">$98.00</div><div class="prod-actions"><span><svg width="14" height="14" viewBox="0 0 16 16"><path d="M8 14 2 8a3.3 3.3 0 0 1 6-4 3.3 3.3 0 0 1 6 4z" fill="#fff"/></svg></span><span><svg width="14" height="14" viewBox="0 0 16 16"><path d="M1 2h2l2 8h8l2-6H4" fill="none" stroke="#fff" stroke-width="1.8"/></svg></span><span><svg width="14" height="14" viewBox="0 0 14 14"><circle cx="6" cy="6" r="4.5" fill="none" stroke="#fff" stroke-width="1.8"/><line x1="9.5" y1="9.5" x2="13" y2="13" stroke="#fff" stroke-width="1.8"/></svg></span></div></div>
</div>
<div class="side-arrows abs"><span class="on"><svg width="12" height="12" viewBox="0 0 12 12"><path d="M3 8l3-4 3 4" fill="none" stroke="#fff" stroke-width="2"/></svg></span><span class="off"><svg width="12" height="12" viewBox="0 0 12 12"><path d="M3 4l3 4 3-4" fill="none" stroke="#fff" stroke-width="2"/></svg></span></div>
<svg class="scroll-hint-2 abs" width="24" height="24" viewBox="0 0 24 24"><path d="M7 10l5 5 5-5" fill="none" stroke="#1c1f33" stroke-width="2"/></svg>

<!-- Product of the month -->
<section class="potm abs">
  <div class="potm-photo abs" role="img" aria-label="Sportswear shop with walls of colourful jackets"></div>
  <svg class="potm-band abs" width="700" height="510" viewBox="0 0 700 510"><polygon points="0,0 640,0 560,510 0,510" fill="#8c1230"/></svg>
  <div class="potm-copy abs">
    <h2 class="heading">Product of the Month</h2>
    <p>Sed ut perspiciatis unde omnis iste natus error sit voluptatem accusantium doloremque laudantium, totam rem aperiam, eaque ipsa quae.</p>
    <div class="potm-deal"><span class="big">25% OFF</span><span class="small">SALE IS ON!</span></div>
    <div class="potm-note">** 20% off sitewide using TEES20 at checkout **</div>
    <span class="btn btn-white">Shop Now</span>
  </div>
</section>

<!-- Testimonials -->
<h2 class="rev-title section-title heading abs">What Our Customer Says<div class="title-bar"></div></h2>
<div class="rev-list abs">
  <div class="review"><p>“Sed ut perspiciatis unde omnis iste natus error sit voluptatem accusantium doloremque laudantium, totam rem aperiam, eaque ipsa quae ab illo inventore veritatis et quasi architecto beatae vitae dicta sunt.”</p><div class="stars"><svg width="84" height="14" viewBox="0 0 84 14"><g fill="#8c1230"><path id="st" d="M7 0l2 5h5l-4 3 2 5-5-3-5 3 2-5-4-3h5z"/><use href="#st" x="17"/><use href="#st" x="34"/><use href="#st" x="51"/></g><use href="#st" x="68" fill="#ddd"/></svg></div><div class="reviewer"><span class="avatar" role="img" aria-label="Customer portrait"></span><div><b>Marcus T. Hale</b><small>Lorem ipsum dolor</small></div></div></div>
  <div class="review featured"><p>“Sed ut perspiciatis unde omnis iste natus error sit voluptatem accusantium doloremque laudantium, totam rem aperiam, eaque ipsa quae ab illo inventore veritatis et quasi architecto beatae vitae dicta sunt.”</p><div class="stars"><svg width="84" height="14" viewBox="0 0 84 14"><g fill="#8c1230"><use href="#st"/><use href="#st" x="17"/><use href="#st" x="34"/><use href="#st" x="51"/></g><use href="#st" x="68" fill="#ddd"/></svg></div><div class="reviewer"><span class="avatar" role="img" aria-label="Customer portrait"></span><div><b>Marcus T. Hale</b><small>Lorem ipsum dolor</small></div></div></div>
  <div class="review"><p>“Sed ut perspiciatis unde omnis iste natus error sit voluptatem accusantium doloremque laudantium, totam rem aperiam, eaque ipsa quae ab illo inventore veritatis et quasi architecto beatae vitae dicta sunt.”</p><div class="stars"><svg width="84" height="14" viewBox="0 0 84 14"><g fill="#8c1230"><use href="#st"/><use href="#st" x="17"/><use href="#st" x="34"/><use href="#st" x="51"/></g><use href="#st" x="68" fill="#ddd"/></svg></div><div class="reviewer"><span class="avatar" role="img" aria-label="Customer portrait"></span><div><b>Marcus T. Hale</b><small>Lorem ipsum dolor</small></div></div></div>
</div>
<div class="side-arrows rev-arrows abs"><span class="on"><svg width="12" height="12" viewBox="0 0 12 12"><path d="M3 8l3-4 3 4" fill="none" stroke="#fff" stroke-width="2"/></svg></span><span class="off"><svg width="12" height="12" viewBox="0 0 12 12"><path d="M3 4l3 4 3-4" fill="none" stroke="#fff" stroke-width="2"/></svg></span></div>

<!-- Newsletter -->
<section class="newsletter abs"></section>
<h2 class="nl-title heading abs">Subscribe to<br>Join Our Newsletter</h2>
<div class="nl-label abs">GET 10% OFF YOUR FIRST ORDER!</div>
<div class="nl-form abs"><div class="nl-input">Email Address</div><div class="nl-btn"><svg width="16" height="16" viewBox="0 0 16 16"><path d="M6 3l5 5-5 5" fill="none" stroke="#fff" stroke-width="2"/></svg></div></div>

<!-- Footer -->
<div class="brand foot-brand abs"><span class="brand-square"></span><div class="brand-name">KELVO-TRA<small>BRAND</small></div></div>
<div class="socials abs"><span></span><span></span><span></span><span></span></div>
<div class="foot-col abs" style="left:408px"><h4>Quick Links</h4><div class="title-bar"></div><ul><li>Home</li><li>Shop By Categories</li><li>Products</li><li>Reviews</li><li>Contact Us</li></ul></div>
<div class="foot-col abs" style="left:646px"><h4>Product Categories</h4><div class="title-bar"></div><ul><li>Hoodies</li><li>Activewear</li><li>Footwear</li><li>Accessories</li><li>Winter Collection</li></ul></div>
<div class="foot-col abs" style="left:904px"><h4>Terms &amp; Conditions</h4><div class="title-bar"></div><ul><li>Store Policy</li><li>Shipping</li><li>Return Policy</li><li>Payment Methods</li></ul></div>
<div class="payments abs"><span></span><span></span><span></span><span></span><span></span><span></span><span></span></div>
<div class="bottom-bar abs"><span>© COPYRIGHT | ALL RIGHTS RESERVED</span><span>TERMS &amp; CONDITIONS</span></div>

</body>
</html>
```